PDF Document Update

Hi,

I need the attached PDF document updated.

The word document attached outlines the new format for which I want the PDF to look like.

For the "Our People" section - please remove Wilma Brackett and add in Owen Pellow (his photo is also attached).

Thanks!

```html
<!DOCTYPE html>
<html lang="en">
<head>
<meta charset="utf-8">
<title>Harbourline Talent – Corporate Overview</title>
<link rel="stylesheet" href="https://fonts.googleapis.com/css2?family=Cormorant+Garamond:wght@500;600&family=Open+Sans:wght@400;600&display=swap">
<style>
  :root {
    --backdrop: #d7d6db;
    --paper: #ffffff;
    --navy: #0b1c45;
    --brand-blue: #1d3f94;
    --photo-light: #6aa6d8;
    --photo-deep: #3a6fa6;
    --text-light: #e6e9f2;
  }
  * { box-sizing: border-box; margin: 0; padding: 0; }
  html, body {
    width: 1200px; height: 826px; overflow: hidden;
    background: var(--backdrop);
  }
  .canvas {
    position: relative; width: 1200px; height: 826px;
    display: flex; align-items: center; justify-content: center;
  }
  .page {
    position: relative; width: 580px; height: 790px;
    background: var(--paper);
    box-shadow: 0 12px 30px rgba(0,0,0,0.18);
    overflow: hidden;
  }
  .hero-photo {
    position: absolute; left: 0; top: 0; width: 100%; height: 470px;
    background: linear-gradient(180deg, var(--photo-light) 0%, var(--photo-deep) 100%);
  }
  .corner-panel {
    position: absolute; left: 0; top: 0; width: 210px; height: 340px;
  }
  .brand {
    position: absolute; left: 34px; top: 168px;
    display: flex; align-items: flex-start; gap: 8px;
    font-family: "Cormorant Garamond", serif; font-weight: 600;
    font-size: 18px; line-height: 1.05; color: var(--brand-blue);
    letter-spacing: 0.3px;
  }
  .brand-square { width: 12px; height: 12px; margin-top: 4px; background: var(--brand-blue); flex: none; }
  .overview {
    position: absolute; left: 0; top: 440px; width: 100%; height: 312px;
    background: var(--navy);
    padding: 52px 56px 0;
    text-align: center; color: var(--text-light);
  }
  .overview-title {
    font-family: "Cormorant Garamond", serif; font-weight: 500;
    font-size: 30px; letter-spacing: 3px; color: #fff;
    margin-bottom: 26px;
  }
  .overview-text {
    font-family: "Open Sans", sans-serif; font-size: 10.5px; line-height: 1.65;
    margin-bottom: 14px;
  }
  .overview-text strong { font-weight: 600; color: #fff; }
  .page-footer {
    position: absolute; left: 0; bottom: 0; width: 100%; height: 38px;
    display: flex; align-items: center; justify-content: center;
    font-family: "Open Sans", sans-serif; font-size: 10px; color: var(--navy);
    letter-spacing: 0.3px;
  }
  .page-footer .divider { margin: 0 8px; }
</style>
</head>
<body>
<main class="canvas">
  <article class="page">
    <div class="hero-photo" role="img" aria-label="Photograph of a harbourside opera house with white sail roofs under a blue sky, above the water"></div>

    <svg class="corner-panel" viewBox="0 0 210 340" aria-hidden="true">
      <path d="M0 0 H150 Q200 0 196 60 L150 340 H0 Z" fill="#ffffff"/>
    </svg>

    <div class="brand">
      <span class="brand-square"></span>
      <span class="brand-name">Harbourline<br>Talent</span>
    </div>

    <section class="overview">
      <h1 class="overview-title">CORPORATE OVERVIEW</h1>
      <p class="overview-text"><strong>Harbourline Talent</strong> is an Australian recruitment firm and trusted recruitment partner to financial services firms, blue-chip corporates and professional services practices across Asia Pacific.</p>
      <p class="overview-text">We add value by leveraging our deep understanding of the industries, markets and disciplines that we serve, enabling us to present an informed and honest approach when providing recruitment advice. We remain focused on the belief that in any recruitment process diligence, honesty and integrity will always ensure the best outcome.</p>
    </section>

    <footer class="page-footer">
      <span>www.harbourlinetalent.com.au</span>
      <span class="divider">|</span>
      <span>info@harbourlinetalent.com.au</span>
    </footer>
  </article>
</main>
</body>
</html>
```